wine bottle label design

My girlfriend and I are getting married. We are sending out invitations, in a wine bottle. For that we need a label on the bottle.
Our names are Mette & Jørgen. We would like the M and J to somehow play a bigger part in the logo.
Also maybe with an Illustration (best if made as a drawing resembling the church we are getting married in) https://www.fjordtonerne.dk/index.php/kalender/83-uncategorised/148-gospelgudstjeneste-i-dalbro-kirke.html

Bryllup den 27 april 2019, kl. 14:00 i Dalbro Kirke

Decorative

```html
<!DOCTYPE html>
<html lang="da">
<head>
<meta charset="utf-8">
<title>Mette &amp; Jørgen – vinetiket</title>
<link rel="stylesheet" href="https://fonts.googleapis.com/css2?family=Fira+Sans:wght@400;500&family=Cormorant+Garamond:ital,wght@1,500&display=swap">
<style>
  :root {
    --backdrop: #f5e9d8;
    --label: #0a0b0c;
    --gold: #b39a5c;
    --gold-bright: #d8b54a;
    --ink-light: #f4f1ea;
    --arrow: #cfcac0;
  }
  * { margin: 0; padding: 0; box-sizing: border-box; }
  html, body {
    width: 1200px; height: 1200px; overflow: hidden;
    background: var(--backdrop);
  }
  .label {
    position: absolute; left: 240px; top: 100px;
    width: 720px; height: 1000px;
    background: var(--label);
    overflow: hidden;
  }
  .speckle {
    position: absolute;
    background: radial-gradient(ellipse at center, rgba(179,154,92,.55) 0%, rgba(179,154,92,.18) 55%, rgba(179,154,92,0) 75%);
  }
  .speckle--top-left { left: -40px; top: -30px; width: 320px; height: 240px; }
  .speckle--top-right { left: 460px; top: 90px; width: 300px; height: 250px; }
  .speckle--bottom-left { left: -50px; top: 660px; width: 280px; height: 260px; }
  .speckle--bottom-right { left: 380px; top: 800px; width: 380px; height: 240px; }
  .ornament {
    position: absolute; left: 270px; top: 150px;
    width: 180px; height: 34px;
    border-radius: 17px;
    background: linear-gradient(90deg, rgba(216,181,74,0) 0%, rgba(216,181,74,.7) 35%, rgba(216,181,74,.9) 50%, rgba(216,181,74,.7) 65%, rgba(216,181,74,0) 100%);
  }
  .tagline {
    position: absolute; left: 0; width: 100%; top: 210px;
    text-align: center;
    font-family: "Fira Sans", sans-serif; font-weight: 400;
    font-size: 26px; letter-spacing: .22em;
    color: var(--ink-light);
  }
  .name {
    position: absolute;
    font-family: "Fira Sans", sans-serif; font-weight: 500;
    font-size: 160px; line-height: 1;
    color: var(--gold);
  }
  .name--bride { left: 170px; top: 270px; }
  .name--groom { left: 110px; top: 520px; }
  .ampersand {
    position: absolute; left: 330px; top: 440px;
    font-family: "Fira Sans", sans-serif; font-weight: 500;
    font-size: 80px; line-height: 1;
    color: var(--gold-bright);
  }
  .arrow { position: absolute; width: 160px; height: 40px; }
  .arrow--right { left: 130px; top: 465px; }
  .arrow--left { left: 470px; top: 510px; }
  .details {
    position: absolute; left: 0; width: 100%; top: 720px;
    text-align: center;
    font-family: "Cormorant Garamond", serif; font-style: italic; font-weight: 500;
    font-size: 42px; line-height: 1.12;
    color: var(--ink-light);
  }
</style>
</head>
<body>
  <main class="label">
    <div class="speckle speckle--top-left" role="img" aria-label="Scattered gold dot pattern"></div>
    <div class="speckle speckle--top-right" role="img" aria-label="Scattered gold dot pattern"></div>
    <div class="speckle speckle--bottom-left" role="img" aria-label="Scattered gold dot pattern"></div>
    <div class="speckle speckle--bottom-right" role="img" aria-label="Scattered gold dot pattern"></div>

    <div class="ornament" role="img" aria-label="Gold floral ornament with rose and leafy branches"></div>
    <p class="tagline">A TOAST TO LOVE</p>

    <h1 class="name name--bride">Mette</h1>
    <svg class="arrow arrow--right" viewBox="0 0 160 40" aria-hidden="true">
      <g fill="none" stroke="var(--arrow)" stroke-width="2.5" stroke-linecap="round">
        <line x1="10" y1="20" x2="150" y2="20"/>
        <polyline points="138,10 150,20 138,30"/>
        <polyline points="6,10 16,20 6,30"/>
        <polyline points="18,10 28,20 18,30"/>
      </g>
    </svg>
    <span class="ampersand">&amp;</span>
    <svg class="arrow arrow--left" viewBox="0 0 160 40" aria-hidden="true">
      <g fill="none" stroke="var(--arrow)" stroke-width="2.5" stroke-linecap="round">
        <line x1="10" y1="20" x2="150" y2="20"/>
        <polyline points="22,10 10,20 22,30"/>
        <polyline points="154,10 144,20 154,30"/>
        <polyline points="142,10 132,20 142,30"/>
      </g>
    </svg>
    <h1 class="name name--groom">Jørgen</h1>

    <p class="details">Bryllup den<br>27 april 2019, kl.<br>14:00 i Dalbro Kirke</p>
  </main>
</body>
</html>
```